Delivery Performance Dashboard for Web Portal

We need you to design a dashboard for our web portal. We deliver sand and stone to construction jobsites. The attached screenshot is from our current web portal dashboard . It shows how much material has been delivered from an order.

Dump trucks will deliver multiple loads during the day and the dispatcher uses the dashboard to monitor if they need to add more trucks or less trucks to fulfill the order. An example would be, I need to ship 1,000 tons of sand to a jobsite and I plan to use 10 trucks during the day and that it will take 10 hours of hauling to complete the job. After 5 hours of hauling (50% the day is over), I should have delivered 500 tons of sand (50% of the order). But maybe there is a lot of traffic, and I only have delivered 300 tons. The dashboard will show that I am behind schedule and I might need to add 2 more trucks to the job.

Industry/Entity Type

Construction

Font styles to use
Sans Serif

Requirements
Must have
• We need a progress bar showing how much material has been delivered, how much material was requested to be delivered total and how much material should have been delivered at the current time. The goal is to show the user if the deliveries are ahead or behind the expected pace and why.
Nice to have
• The icons for plant, driving and jobsite show if the actual times have exceeded or beaten the planned times. Maybe you have other ideas to show the user if the trucks are sitting longer on the jobsite, at the plant to get loaded or driving to and from the jobsite.

```html
<!DOCTYPE html>
<html lang="en">
<head>
<meta charset="utf-8">
<title>Delivery Performance Dashboard</title>
<link href="https://fonts.googleapis.com/css2?family=Roboto:wght@400;500;700&display=swap" rel="stylesheet">
<style>
  :root {
    --ink: #111418;
    --muted: #8a8d92;
    --soft: #a9acb1;
    --line: #e3e5e8;
    --field: #f1f4f7;
    --page: #f8f9fb;
    --white: #ffffff;
    --head: #e4e5e7;
    --cyan: #00c2ec;
    --green: #2fd083;
    --tick: #2ecc71;
    --red: #f01010;
    --track: #e9eaec;
    --grey-icon: #7c7f84;
  }
  * { box-sizing: border-box; margin: 0; padding: 0; }
  html, body { width: 1200px; height: 675px; overflow: hidden; }
  body { font-family: "Roboto", Arial, sans-serif; background: var(--page); color: var(--ink); position: relative; }

  .topbar { position: absolute; left: 0; top: 0; width: 1200px; height: 75px; background: var(--white); border-bottom: 1px solid var(--line); }
  .brand { position: absolute; left: 73px; top: 32px; font-size: 14px; font-weight: 700; letter-spacing: .1px; }
  .top-search { position: absolute; left: 808px; top: 32px; display: flex; align-items: center; gap: 8px; font-size: 13px; color: #333; }
  .bell { position: absolute; left: 925px; top: 33px; }
  .avatar { position: absolute; left: 978px; top: 23px; width: 34px; height: 34px; border-radius: 50%; background: radial-gradient(circle at 50% 40%, #c79c80, #6b5a4e); }
  .user { position: absolute; left: 1027px; top: 32px; font-size: 14px; font-weight: 700; }

  .filters { position: absolute; left: 0; top: 76px; width: 1200px; height: 75px; background: var(--white); }
  .field { position: absolute; top: 24px; height: 28px; background: var(--field); border-radius: 2px; display: flex; align-items: center; justify-content: space-between; padding: 0 10px; font-size: 12.5px; color: var(--soft); }
  .filter-label { position: absolute; top: 31px; font-size: 12.5px; font-weight: 700; color: var(--ink); }
  .dash { position: absolute; left: 950px; top: 30px; font-size: 13px; color: #444; }

  .table { position: absolute; left: 73px; top: 190px; width: 1054px; }
  .row { display: grid; grid-template-columns: 73px 161px 108px 132px 86px 164px 153px 177px; }
  .table-head { height: 40px; background: var(--head); align-items: center; }
  .table-head .th { height: 100%; display: flex; align-items: center; gap: 6px; font-size: 14px; font-weight: 700; padding-left: 11px; border-right: 1px solid #f4f4f5; }
  .table-head .th:last-child { border-right: none; }
  .th svg { flex: none; }

  .order-row { height: 73px; background: var(--white); margin-top: 5px; }
  .cell { display: flex; flex-direction: column; justify-content: center; padding-left: 13px; border-right: 1px solid var(--line); margin: 10px 0; }
  .cell:last-child { border-right: none; }
  .order-id { font-size: 13px; font-weight: 700; color: var(--muted); }
  .customer { font-size: 13.5px; font-weight: 700; color: var(--ink); line-height: 16px; }
  .division, .place { font-size: 12px; font-weight: 700; color: var(--soft); line-height: 15px; }
  .status { align-items: center; padding-left: 0; gap: 3px; font-size: 12.5px; font-weight: 700; color: var(--muted); }

  .progress { padding-left: 21px; }
  .bar-line { display: flex; align-items: center; gap: 4px; height: 12px; }
  .track { width: 93px; height: 7px; border-radius: 4px; background: var(--track); overflow: hidden; }
  .fill { height: 100%; background: var(--cyan); border-radius: 4px; }
  .pct { font-size: 10px; }
  .pct.bad { color: var(--red); }
  .pct.good { color: var(--green); }
  .nums { display: flex; width: 93px; justify-content: space-between; font-size: 8.5px; color: #222; margin-top: 5px; }
  .units { display: flex; width: 93px; justify-content: space-between; font-size: 8px; color: var(--muted); margin-top: 3px; }

  .remarks { flex-direction: row; align-items: center; justify-content: flex-start; gap: 14px; padding-left: 20px; }
  .remark-body { width: 83px; }
  .remark-title { font-size: 9px; font-weight: 700; line-height: 11px; margin-bottom: 3px; }
  .remark-title.bad { color: var(--red); }
  .remark-title.good { color: var(--green); }
  .remark-bar { height: 8px; border-radius: 4px; background: var(--field); overflow: hidden; }
  .remark-fill { height: 100%; border-radius: 4px; }
  .remark-fill.bad { background: var(--red); }
  .remark-fill.good { background: var(--green); }
  .remark-note { font-size: 9px; font-weight: 700; color: var(--green); margin-top: 4px; padding-left: 2px; }
</style>
</head>
<body>

<header class="topbar">
  <div class="brand">COMPANY NAME</div>
  <div class="top-search">
    <svg width="16" height="16" viewBox="0 0 16 16" fill="none" stroke="#111" stroke-width="1.8"><circle cx="7" cy="7" r="5.5"/><path d="M11 11l4 4"/></svg>
    Search
  </div>
  <svg class="bell" width="14" height="16" viewBox="0 0 14 16" fill="none" stroke="#111" stroke-width="1.2"><path d="M2 12V7a5 5 0 0 1 10 0v5l1 1H1z"/><path d="M5.5 14.5a1.5 1.5 0 0 0 3 0"/></svg>
  <div class="avatar" role="img" aria-label="Dispatcher profile photo"></div>
  <div class="user">Dispatcher A</div>
</header>

<section class="filters">
  <div class="field" style="left:73px;width:216px;">Search order
    <svg width="15" height="15" viewBox="0 0 16 16" fill="none" stroke="#777" stroke-width="1.5"><circle cx="7" cy="7" r="5.5"/><path d="M11 11l4 4"/></svg>
  </div>
  <div class="filter-label" style="left:359px;">Status</div>
  <div class="field" style="left:403px;width:83px;color:var(--muted);">Active
    <svg width="11" height="7" viewBox="0 0 11 7" fill="none" stroke="#666" stroke-width="1.3"><path d="M1 1l4.5 4.5L10 1"/></svg>
  </div>
  <div class="filter-label" style="left:569px;">Location</div>
  <div class="field" style="left:626px;width:105px;">New York
    <svg width="11" height="7" viewBox="0 0 11 7" fill="none" stroke="#666" stroke-width="1.3"><path d="M1 1l4.5 4.5L10 1"/></svg>
  </div>
  <div class="filter-label" style="left:794px;">Date</div>
  <div class="field" style="left:831px;width:111px;">1 Jul 2020
    <svg width="13" height="13" viewBox="0 0 13 13" fill="#888"><rect x="0" y="2" width="13" height="11" rx="1"/><rect x="1.5" y="5" width="10" height="6.5" fill="#f1f4f7"/><rect x="3" y="6.5" width="2" height="1.5"/><rect x="6" y="6.5" width="2" height="1.5"/><rect x="3" y="9" width="2" height="1.5"/><rect x="6" y="9" width="2" height="1.5"/><rect x="9" y="6.5" width="1.5" height="1.5"/></svg>
  </div>
  <div class="dash">-</div>
  <div class="field" style="left:961px;width:111px;">2 Jul 2020
    <svg width="13" height="13" viewBox="0 0 13 13" fill="#888"><rect x="0" y="2" width="13" height="11" rx="1"/><rect x="1.5" y="5" width="10" height="6.5" fill="#f1f4f7"/><rect x="3" y="6.5" width="2" height="1.5"/><rect x="6" y="6.5" width="2" height="1.5"/><rect x="3" y="9" width="2" height="1.5"/><rect x="6" y="9" width="2" height="1.5"/><rect x="9" y="6.5" width="1.5" height="1.5"/></svg>
  </div>
</section>

<svg width="0" height="0" style="position:absolute">
  <defs>
    <symbol id="dump-truck" viewBox="0 0 42 28">
      <g fill="none" stroke="#00c2ec" stroke-width="1.5">
        <path d="M12 5c4-4 22-4 28 0v14H12z"/>
        <path d="M17 8v9M21 8v9M25 8v9M29 8v9M33 8v9"/>
        <path d="M2 19V12l3-4h7v11"/>
        <path d="M4 12h6"/>
        <path d="M1 19h40"/>
        <circle cx="7" cy="23" r="3"/><circle cx="24" cy="23" r="3"/><circle cx="33" cy="23" r="3"/>
      </g>
    </symbol>
    <symbol id="tick-ok" viewBox="0 0 18 18">
      <circle cx="9" cy="9" r="9" fill="#2ecc71"/><path d="M5 9.3l2.7 2.7L13 6.5" fill="none" stroke="#fff" stroke-width="1.8"/>
    </symbol>
    <symbol id="tick-wait" viewBox="0 0 18 18">
      <circle cx="9" cy="9" r="9" fill="#7c7f84"/><path d="M5 9.3l2.7 2.7L13 6.5" fill="none" stroke="#fff" stroke-width="1.8"/>
    </symbol>
  </defs>
</svg>

<main class="table">
  <div class="row table-head">
    <div class="th"><span style="color:var(--cyan);font-size:22px;font-weight:400;">#</span>Order</div>
    <div class="th"><svg width="18" height="20" viewBox="0 0 18 20" fill="none" stroke="#00c2ec" stroke-width="1.5"><circle cx="9" cy="6" r="4.5"/><path d="M1 19c0-5 3.5-7.5 8-7.5s8 2.5 8 7.5z"/></svg>Customer</div>
    <div class="th"><svg width="28" height="20"><use href="#dump-truck"/></svg>Origin</div>
    <div class="th"><svg width="28" height="20"><use href="#dump-truck"/></svg>Destination</div>
    <div class="th">Status</div>
    <div class="th"><svg width="24" height="20" viewBox="0 0 24 20" fill="none" stroke="#00c2ec" stroke-width="1.4"><path d="M2 15l6-11 12 4-3 7z"/><path d="M1 15h22M4 19h16"/><circle cx="6" cy="17" r="1.5"/><circle cx="18" cy="17" r="1.5"/></svg>Tonnage/Trucks</div>
    <div class="th"><svg width="20" height="20" viewBox="0 0 20 20" fill="none" stroke="#00c2ec" stroke-width="1.4"><rect x="1" y="3" width="16" height="15" rx="1"/><path d="M1 7h16M5 1v4M13 1v4"/><circle cx="15" cy="15" r="4" fill="#e4e5e7"/><path d="M15 13v2h1.5"/></svg>Time</div>
    <div class="th"><svg width="20" height="20" viewBox="0 0 20 20" fill="none" stroke="#00c2ec" stroke-width="1.4"><circle cx="10" cy="10" r="9"/><path d="M7.5 7.5a2.5 2.5 0 1 1 3.5 2.3c-.7.3-1 .8-1 1.6v.6"/><circle cx="10" cy="14.8" r=".6" fill="#00c2ec"/></svg>Remarks</div>
  </div>

  <div class="row order-row">
    <div class="cell"><span class="order-id">#17746</span></div>
    <div class="cell"><span class="customer">Harlan Construction</span><span class="division">North Division</span></div>
    <div class="cell"><span class="place">Ridgeford<br>Asphalt Plant</span></div>
    <div class="cell"><span class="place">KRTV - 240&nbsp; from<br>mm 12 - 36</span></div>
    <div class="cell status"><svg width="17" height="17"><use href="#tick-ok"/></svg>Accepted</div>
    <div class="cell progress">
      <div class="bar-line"><div class="track"><div class="fill" style="width:54%"></div></div><span class="pct bad">30%</span></div>
      <div class="nums"><span>300/1000</span><span>3/10</span></div>
      <div class="units"><span>Tons</span><span>Trucks</span></div>
    </div>
    <div class="cell progress">
      <div class="bar-line"><div class="track"><div class="fill" style="width:54%"></div></div><span class="pct bad">30%</span></div>
      <div class="nums"><span>3/10</span></div>
      <div class="units"><span>Time(Hrs)</span></div>
    </div>
    <div class="cell remarks">
      <svg width="42" height="28"><use href="#dump-truck"/></svg>
      <div class="remark-body">
        <div class="remark-title bad">Oops! Running behind Schedule</div>
        <div class="remark-bar"><div class="remark-fill bad" style="width:76%"></div></div>
        <div class="remark-note">Add 2 More Trucks</div>
      </div>
    </div>
  </div>

  <div class="row order-row">
    <div class="cell"><span class="order-id">#17746</span></div>
    <div class="cell"><span class="customer">Harlan Construction</span><span class="division">North Division</span></div>
    <div class="cell"><span class="place">Ridgeford<br>Asphalt Plant</span></div>
    <div class="cell"><span class="place">KRTV - 240&nbsp; from<br>mm 12 - 36</span></div>
    <div class="cell status"><svg width="17" height="17"><use href="#tick-ok"/></svg>Accepted</div>
    <div class="cell progress">
      <div class="bar-line"><div class="track"><div class="fill" style="width:77%"></div></div><span class="pct good">30%</span></div>
      <div class="nums"><span>300/1000</span><span>3/10</span></div>
      <div class="units"><span>Tons</span><span>Trucks</span></div>
    </div>
    <div class="cell progress">
      <div class="bar-line"><div class="track"><div class="fill" style="width:84%"></div></div><span class="pct good">30%</span></div>
      <div class="nums"><span>3/10</span></div>
      <div class="units"><span>Time(Hrs)</span></div>
    </div>
    <div class="cell remarks">
      <svg width="42" height="28"><use href="#dump-truck"/></svg>
      <div class="remark-body">
        <div class="remark-title good">Good! on Schedule</div>
        <div class="remark-bar"><div class="remark-fill good" style="width:77%"></div></div>
      </div>
    </div>
  </div>

  <div class="row order-row">
    <div class="cell"><span class="order-id">#17746</span></div>
    <div class="cell"><span class="customer">Harlan Construction</span><span class="division">North Division</span></div>
    <div class="cell"><span class="place">Ridgeford<br>Asphalt Plant</span></div>
    <div class="cell"><span class="place">KRTV - 240&nbsp; from<br>mm 12 - 36</span></div>
    <div class="cell status"><svg width="17" height="17"><use href="#tick-ok"/></svg>Accepted</div>
    <div class="cell progress">
      <div class="bar-line"><div class="track"><div class="fill" style="width:100%"></div></div><span class="pct good">100%</span></div>
      <div class="nums"><span>1000/1000</span><span>10/10</span></div>
      <div class="units"><span>Tons</span><span>Trucks</span></div>
    </div>
    <div class="cell progress">
      <div class="bar-line"><div class="track"><div class="fill" style="width:100%"></div></div><span class="pct good">100%</span></div>
      <div class="nums"><span>10/10</span></div>
      <div class="units"><span>Time(Hrs)</span></div>
    </div>
    <div class="cell remarks">
      <svg width="42" height="28"><use href="#dump-truck"/></svg>
      <div class="remark-body">
        <div class="remark-title good">Complete!</div>
        <div class="remark-bar"><div class="remark-fill good" style="width:100%"></div></div>
        <div class="remark-note">Good Job!</div>
      </div>
    </div>
  </div>

  <div class="row order-row">
    <div class="cell"><span class="order-id">#17746</span></div>
    <div class="cell"><span class="customer">Harlan Construction</span><span class="division">North Division</span></div>
    <div class="cell"><span class="place">Ridgeford<br>Asphalt Plant</span></div>
    <div class="cell"><span class="place">KRTV - 240&nbsp; from<br>mm 12 - 36</span></div>
    <div class="cell status"><svg width="17" height="17"><use href="#tick-wait"/></svg>Pending</div>
    <div class="cell progress">
      <div class="bar-line"><div class="track"></div><span class="pct bad">&nbsp;0%</span></div>
      <div class="nums"><span>0/1000</span><span>0/10</span></div>
      <div class="units"><span>Tons</span><span>Trucks</span></div>
    </div>
    <div class="cell progress">
      <div class="bar-line"><div class="track"></div><span class="pct bad">&nbsp;0%</span></div>
      <div class="nums"><span>0/10</span></div>
      <div class="units"><span>Time(Hrs)</span></div>
    </div>
    <div class="cell remarks">
      <svg width="42" height="28"><use href="#dump-truck"/></svg>
      <div class="remark-body">
        <div class="remark-title bad">Pending</div>
        <div class="remark-bar"></div>
      </div>
    </div>
  </div>

  <div class="row order-row">
    <div class="cell"><span class="order-id">#17746</span></div>
    <div class="cell"><span class="customer">Harlan Construction</span><span class="division">North Division</span></div>
    <div class="cell"><span class="place">Ridgeford<br>Asphalt Plant</span></div>
    <div class="cell"><span class="place">KRTV - 240&nbsp; from<br>mm 12 - 36</span></div>
    <div class="cell status"><svg width="17" height="17"><use href="#tick-ok"/></svg>Accepted</div>
    <div class="cell progress">
      <div class="bar-line"><div class="track"><div class="fill" style="width:54%"></div></div><span class="pct bad">30%</span></div>
      <div class="nums"><span>300/1000</span><span>3/10</span></div>
      <div class="units"><span>Tons</span><span>Trucks</span></div>
    </div>
    <div class="cell progress">
      <div class="bar-line"><div class="track"><div class="fill" style="width:54%"></div></div><span class="pct bad">30%</span></div>
      <div class="nums"><span>3/10</span></div>
      <div class="units"><span>Time(Hrs)</span></div>
    </div>
    <div class="cell remarks">
      <svg width="42" height="28"><use href="#dump-truck"/></svg>
      <div class="remark-body">
        <div class="remark-title bad">Oops! Running behind Schedule</div>
        <div class="remark-bar"><div class="remark-fill bad" style="width:76%"></div></div>
        <div class="remark-note">Add 2 More Trucks</div>
      </div>
    </div>
  </div>
</main>

</body>
</html>
```